Land Development Company Website Redesign

We are looking for a fresh design for our website. The content will remain 90% the same.

We really like the layout style of www.kelvarno.com.

We have attached our current site for content.

Industry/Entity Type

Real Estate Development

Coding

Coded - Design and coding required

Number of Pages Required

5+ page

Font styles to use
Sans Serif

Requirements
Must have
• Consistent feel across all the pages. Visually appealing and simple layout design that can be viewed on a mobile device and browser.

```html
<!DOCTYPE html>
<html lang="en">
<head>
<meta charset="utf-8">
<title>Ridgeholt Estates</title>
<link href="https://fonts.googleapis.com/css2?family=Oswald:wght@500;600&family=Roboto+Condensed:ital,wght@0,400;0,700;1,400&family=Arimo:wght@400;700&display=swap" rel="stylesheet">
<style>
:root{
  --wine:#7a1428;
  --wine-deep:#6b1020;
  --sand:#d4ccaf;
  --cream:#f7f2ea;
  --ink:#333;
  --muted:#8a8a8a;
  --rule:#dedede;
  --black:#050505;
  --grey:#5c5c5c;
  --hero-top:#a9d3d5;
  --hero-mid:#b7b79c;
  --hero-low:#7c8a58;
}
*{box-sizing:border-box;margin:0;padding:0}
html,body{width:922px;height:1200px;overflow:hidden;background:#fff}
body{position:relative;font-family:"Roboto Condensed",sans-serif;color:var(--ink)}
.abs{position:absolute}
.topline{left:0;top:0;width:922px;height:4px;background:var(--wine-deep)}
.header{left:0;top:4px;width:922px;height:65px;border-bottom:1px solid var(--rule)}
.brand{left:195px;top:14px;display:flex;align-items:center;gap:6px;font-family:"Roboto Condensed",sans-serif;font-weight:700;font-size:15px;color:var(--wine)}
.brand i{display:block;width:14px;height:14px;background:var(--wine)}
.nav{left:312px;top:4px;height:65px;display:flex}
.nav a{display:flex;align-items:center;justify-content:center;height:65px;border-left:1px solid var(--rule);font-size:8.5px;color:#222;text-decoration:none;text-transform:uppercase}
.nav a:last-child{border-right:1px solid var(--rule)}
.hero{left:0;top:69px;width:922px;height:347px;background:linear-gradient(180deg,var(--hero-top) 0%,var(--hero-mid) 60%,var(--hero-low) 100%)}
.tag{left:172px;background:var(--wine);color:#fff;text-transform:uppercase;display:flex;align-items:center;padding-left:7px}
.tag.t1{top:141px;width:253px;height:32px;font-family:"Oswald",sans-serif;font-weight:500;font-size:18px}
.tag.t2{top:179px;width:335px;height:23px;font-size:13px}
.tag.t3{top:208px;width:335px;height:23px;font-size:11.5px}
.band{left:0;top:416px;width:922px;height:36px;background:var(--sand)}
.welcome{left:172px;top:416px;width:219px;height:36px;background:var(--wine);color:#fff;font-size:13px;display:flex;align-items:center;padding-left:9px}
.welcome em{margin-left:4px}
.intro{left:172px;top:469px;width:300px;font-size:9.4px;line-height:13.8px}
.intro p+p{margin-top:14px}
.hurry{left:172px;top:601px;width:300px;font-family:"Oswald",sans-serif;font-weight:600;font-size:16px;line-height:20px;color:var(--wine);text-transform:uppercase}
.video{left:515px;top:472px;width:234px;height:164px;background:#000}
.video .frame{position:absolute;left:0;top:33px;width:234px;height:100px;background:linear-gradient(135deg,#6d7f88,#cfd3d2 45%,#3e4a52)}
.video .controls{position:absolute;left:0;top:143px;width:234px;height:21px;display:flex;align-items:center;gap:8px;padding:0 8px;color:#bbb;font-size:6px}
.section-title{left:172px;top:675px;font-size:11.5px;text-transform:uppercase;color:#333}
.underline{left:172px;top:689px;width:237px;height:4px;background:var(--sand)}
.underline i{display:block;width:90px;height:4px;background:var(--wine)}
.news-panel{left:172px;top:705px;width:235px;height:340px;background:var(--cream)}
.news-box{left:180px;width:219px;height:158px;border:1px solid var(--wine);background:#fff;font-family:"Arimo",sans-serif}
.news-box h3{font-size:7.2px;color:var(--wine);letter-spacing:.4px;padding:9px 0 0 9px;height:22px;border-bottom:1px solid #ccc;margin:0 3px}
.news-box ul{list-style:none;padding:3px 0 0 8px}
.news-box li{position:relative;padding-left:10px;height:35px;padding-top:6px;font-size:6.6px;color:#444;letter-spacing:.3px}
.news-box li span{display:block;margin-top:6px}
.news-box li::before,.news-box .more::before{content:"";position:absolute;left:0;top:7px;border-left:5px solid #222;border-top:3px solid transparent;border-bottom:3px solid transparent}
.news-box .more{position:absolute;left:3px;right:3px;top:133px;border-top:1px solid #ccc;padding:8px 0 0 18px;font-size:6.6px;letter-spacing:.4px;color:#333;text-decoration:underline}
.news-box .more::before{left:6px;top:10px}
.tab-panel{left:430px;top:676px;width:319px;height:371px;background:var(--cream)}
.tab-box{left:439px;top:687px;width:297px;height:341px;border:1px solid var(--wine);background:#fff}
.tab{top:687px;height:24px;display:flex;align-items:center;justify-content:center;font-size:8.5px;text-transform:uppercase;color:#fff;background:var(--wine)}
.tab.active{background:#fff;color:#222;border:1px solid var(--wine);border-bottom:none}
.tab-text{left:447px;top:740px;width:280px;font-family:"Arimo",sans-serif;font-size:8px;line-height:15px;color:#333}
.tab-photo{left:447px;top:873px;width:278px;height:145px;background:linear-gradient(135deg,#4a3524 0%,#a97d4f 50%,#33445c 100%)}
.foot-red{left:0;top:1050px;width:922px;height:15px;background:var(--wine-deep)}
.foot{left:0;top:1065px;width:922px;height:107px;background:var(--black)}
.foot-col{top:1076px;font-family:"Arimo",sans-serif;font-size:7.6px;color:var(--muted);line-height:15.2px}
.foot-col h4{font-weight:400;color:#bdbdbd;text-transform:uppercase;margin-bottom:0}
.foot-divider{left:572px;top:1076px;width:1px;height:77px;background:#444}
.social{top:1145px;width:19px;height:19px;border:1px solid #999}
.copyright{left:0;top:1172px;width:922px;height:28px;background:var(--grey);color:#1d1d1d;font-family:"Arimo",sans-serif;font-size:7.4px;display:flex;align-items:center;justify-content:center}
</style>
</head>
<body>
<div class="abs topline"></div>
<header class="abs header"></header>
<div class="abs brand"><i></i>Ridgeholt</div>
<nav class="abs nav">
  <a style="width:87px">What's New</a>
  <a style="width:87px">The Estates</a>
  <a style="width:83px">The Team</a>
  <a style="width:81px">Gallery</a>
  <a style="width:99px">Contact</a>
</nav>

<div class="abs hero" role="img" aria-label="Photo of a two-storey family home with a smiling agent presenting it"></div>
<div class="abs tag t1">The Ridgeholt Estates</div>
<div class="abs tag t2">He homes here are architecturally pleasin</div>
<div class="abs tag t3">These lots are impressive with over 90 to 100 feet wide</div>

<div class="abs band"></div>
<div class="abs welcome">Welcome to <em>Ridgeholt Estates vision</em></div>

<div class="abs intro">
  <p>Ridgeholt Estates at Cedar Bend is quickly becoming Marwood's finest custom home community. In spring 2009, 9 of 49 custom homesites will be offering to the public. These lots are impressive with over 90 to 100 feet wide and are ranging from one-quarter to over half an acre in size.</p>
  <p>In order to take advantage of the Pre-Development price, call now to place a fully refundable deposit for a reservation of these home sites.</p>
</div>
<h2 class="abs hurry">Hurry only three custom lots are available!</h2>

<div class="abs video">
  <div class="frame" role="img" aria-label="Video still of a business meeting"></div>
  <svg style="position:absolute;left:98px;top:70px" width="38" height="26" viewBox="0 0 38 26"><rect width="38" height="26" rx="6" fill="#222" opacity=".85"/><path d="M15 7l10 6-10 6z" fill="#fff"/></svg>
  <div style="position:absolute;left:0;top:135px;width:234px;height:3px;background:#444"></div>
  <div style="position:absolute;left:2px;top:133px;width:7px;height:7px;border-radius:50%;background:#ddd"></div>
  <div class="controls">
    <svg width="8" height="8"><path d="M1 0l7 4-7 4z" fill="#ccc"/></svg>
    <svg width="9" height="8"><path d="M0 3h2l3-3v8l-3-3H0z" fill="#ccc"/></svg>
    <span>0:00 / 2:36</span>
  </div>
</div>

<div class="abs section-title">Latest News</div>
<div class="abs underline"><i></i></div>
<div class="abs news-panel"></div>
<div class="abs news-box" style="top:711px">
  <h3>PRESS RELEASES</h3>
  <ul>
    <li>Nov 23/15<span>All future Phases will consist of very limited releases.</span></li>
    <li>Nov 23/15<span>All future Phases will consist of very limited releases.</span></li>
    <li>Nov 23/15<span>All future Phases will consist of very limited releases.</span></li>
  </ul>
  <div class="more">VIEW ALL PRESS RELEASES</div>
</div>
<div class="abs news-box" style="top:878px">
  <h3>RELATED PRESS &amp; MEDIA</h3>
  <ul>
    <li>Nov 23/15<span>All future Phases will consist of very limited releases.</span></li>
    <li>Nov 23/15<span>All future Phases will consist of very limited releases.</span></li>
    <li>Nov 23/15<span>All future Phases will consist of very limited releases.</span></li>
  </ul>
  <div class="more">VIEW ALL PRESS RELEASES</div>
</div>

<div class="abs tab-panel"></div>
<div class="abs tab-box"></div>
<div class="abs tab active" style="left:439px;width:85px">The Estates</div>
<div class="abs tab" style="left:536px;width:86px">The Team</div>
<div class="abs tab" style="left:631px;width:79px">Gallery</div>
<p class="abs tab-text">Looking for the perfect new community in Marwood, California? There's no better location than Ridgeholt Estates, an exclusive luxury custom home community nestled in the heart of Cedar Bend, A Marwood Community with easy access to the best that Harlan/Marwood region has to offer. Within a few miles of this pristine community are an abundance of amenities including trails, parks, and lakes. The North Basin Commerce Park, a newly expanded Larkspur Plaza, and Marwood Community Hospital are only a few miles away with easy access to Route 412.</p>
<div class="abs tab-photo" role="img" aria-label="Lit stone courtyard of a home at dusk"></div>

<div class="abs foot-red"></div>
<footer class="abs foot"></footer>
<div class="abs foot-col" style="left:173px"><h4>About</h4>Company Overview<br>Business Model<br>Acquisition Criteria</div>
<div class="abs foot-col" style="left:275px"><h4>The Team</h4>Management Team<br>Board of Directors<br>Board of Advisors</div>
<div class="abs foot-col" style="left:371px"><h4>Company News</h4>Press Releases<br>Related Press<br>Blog</div>
<div class="abs foot-col" style="left:464px"><h4>Investors</h4>Stock Information<br>SEC Filings<br>Investor's FAQ<br>Analyst Coverage</div>
<div class="abs foot-divider"></div>
<div class="abs foot-col" style="left:585px"><h4>Address:</h4>4210 E. Orchard Lane<br>Marwood, CA 90000<br>Phone:&nbsp;&nbsp;&nbsp;&nbsp;&nbsp;555.014.2280<br>Fax:&nbsp;&nbsp;555.014.2291</div>
<div class="abs social" style="left:173px"></div>
<div class="abs social" style="left:197px"></div>
<div class="abs social" style="left:221px"></div>
<div class="abs copyright">Ridgeholt is a registered trademark of ridgeholt land group in the us. all right reserved</div>
</body>
</html>
```